Business card design needed

the business is HR Consulting, but its for SME businesses who cant afford a permanent HR person. We sell an HR info system to help them meet minimum employment legislation but with this hope they then require us on a monthly subscription to phone or email us for HR advice. We are HR qualified mums working from home

So we will be partners to HR and Payroll systems known as kindle HR and Pluto

Target Market(s)

Small to medium businesses so not black and overly corporate, but having said that many are accounting businesses

Industry/Entity Type

Business

Contact Information for Business Card

Name of the company: Tandem HR

Me:Marta Kovalenko
Title:Managing Director

m: 0437 215 683
e: marta@quillmerehr.com.au
w: www.quillmerehr.com.au

What we do: HR Consulting, HR Systems and support, Payroll Advice

Requirements
Nice to have
• there is a company already out there known as Quartz professionals. I like the leaves at the end as I wanted something different like this to the usual business logos but still professional. I wanted a symbol to show calm, positive, ease flow going up ,etc. but realise they have the leaves and possibly cant copy, or can we?..( kite??, something calm and positive)dont know!!. Green and blue needed to be in it as nature and calm as well. I love the colours of www.stafflanefund.com ( attached the colours), as well as the calm wave line underneath. have a look as while they use green and blue I loved the purple colour thrown in there.Green and blue on their own are so overused. I want vibrant. I want double sided and when on a table I want it to stand out so maybe the purple colour (as per the colours on the fund website) solid on one side with just the 3 services we provide and personal and company name on front but need some creativity from you guys.

```html
<!DOCTYPE html>
<html lang="en">
<head>
<meta charset="utf-8">
<title>Quillmere HR – Business Card</title>
<link href="https://fonts.googleapis.com/css2?family=Open+Sans:wght@400;600&display=swap" rel="stylesheet">
<style>
  :root {
    --page-bg: #ffffff;
    --teal: #1aa0ae;
    --lime: #c7d84e;
    --leaf-green: #a9cf3e;
    --forest: #1f7a2c;
    --white: #ffffff;
    --shadow: rgba(0, 0, 0, 0.16);
  }
  * { box-sizing: border-box; margin: 0; padding: 0; }
  html, body {
    width: 1200px;
    height: 421px;
    overflow: hidden;
    background: var(--page-bg);
    font-family: "Open Sans", Arial, sans-serif;
  }
  .stage { position: relative; width: 1200px; height: 421px; }

  .card-shadow {
    position: absolute;
    top: 352px;
    width: 500px;
    height: 24px;
    background: var(--shadow);
    filter: blur(6px);
  }
  .card-shadow-front { left: 46px; }
  .card-shadow-back { left: 649px; }

  .card {
    position: absolute;
    top: 48px;
    width: 540px;
    height: 312px;
    overflow: hidden;
  }
  .card-front { left: 26px; background: var(--teal); }
  .card-back { left: 629px; background: var(--lime); }

  .wordmark {
    position: absolute;
    display: flex;
    align-items: center;
    color: var(--white);
    font-weight: 400;
    white-space: nowrap;
    line-height: 1;
  }
  .wordmark-dot {
    border-radius: 50%;
    flex: none;
  }
  .card-front .wordmark {
    left: 146px;
    top: 130px;
    font-size: 42px;
  }
  .card-front .wordmark-dot {
    width: 26px; height: 26px; margin-left: 12px;
    background: var(--leaf-green);
  }

  .card-back .wordmark {
    right: 24px;
    top: 52px;
    font-size: 32px;
  }
  .card-back .wordmark-dot {
    width: 18px; height: 18px; margin-left: 9px;
    background: var(--white);
  }

  .person-name {
    position: absolute;
    left: 23px;
    top: 129px;
    font-size: 33px;
    font-weight: 400;
    color: var(--forest);
    letter-spacing: 0.4px;
    line-height: 1.3;
  }
  .person-title {
    position: absolute;
    left: 23px;
    top: 170px;
    font-size: 15px;
    font-weight: 600;
    color: var(--white);
  }
  .contact-list {
    position: absolute;
    left: 21px;
    top: 202px;
    list-style: none;
    color: var(--white);
    font-size: 13px;
    line-height: 20px;
  }
  .contact-list li { display: flex; align-items: center; gap: 6px; }
  .contact-icon { width: 13px; height: 13px; flex: none; }
  .website {
    position: absolute;
    left: 20px;
    top: 240px;
    font-size: 20px;
    color: var(--forest);
    letter-spacing: 0.3px;
  }
</style>
</head>
<body>
<main class="stage">
  <div class="card-shadow card-shadow-front"></div>
  <div class="card-shadow card-shadow-back"></div>

  <section class="card card-front" aria-label="Card front">
    <div class="wordmark">Quillmere HR<span class="wordmark-dot"></span></div>
  </section>

  <section class="card card-back" aria-label="Card back">
    <div class="wordmark">Quillmere HR<span class="wordmark-dot"></span></div>
    <h1 class="person-name">Marta Kovalenko</h1>
    <p class="person-title">Managing Director</p>
    <ul class="contact-list">
      <li>
        <svg class="contact-icon" viewBox="0 0 13 13" aria-hidden="true">
          <rect x="3" y="0.5" width="7" height="12" rx="1.2" fill="none" stroke="#fff" stroke-width="1.2"/>
          <rect x="4.3" y="2" width="4.4" height="6.5" fill="#fff"/>
          <circle cx="6.5" cy="10.5" r="0.8" fill="#fff"/>
        </svg>
        <span>0437 215 683</span>
      </li>
      <li>
        <svg class="contact-icon" viewBox="0 0 13 13" aria-hidden="true">
          <rect x="0.5" y="2.5" width="12" height="8" fill="#fff"/>
          <path d="M0.8 3 L6.5 7.5 L12.2 3" fill="none" stroke="#c7d84e" stroke-width="1"/>
        </svg>
        <span>marta@quillmerehr.com.au</span>
      </li>
    </ul>
    <p class="website">www.quillmerehr.com.au</p>
  </section>
</main>
</body>
</html>
```